Business Card Design

New business card design

Target Market(s)

Residential & Commercial Property Managers

Industry/Entity Type

Plumbing Services

Contact Information for Business Card

Name - Owen Tredgold, title - Director, Phone Number - 0431 862 507, email - owen@rvb-plumbing.com.au, Company ABN - 73 215 904 386,

Font styles to use
Sans Serif

Colors
0054AA
0677BA
7BADD7
CADEEF
E8F1F8

```html
<!DOCTYPE html>
<html lang="en">
<head>
<meta charset="utf-8">
<title>RVB Plumbing Services – Business Card</title>
<link href="https://fonts.googleapis.com/css2?family=Arimo:wght@400;700&display=swap" rel="stylesheet">
<style>
  :root {
    --backdrop: #3d3d3d;
    --card-white: #ffffff;
    --card-dark: #1e232a;
    --ink: #1e232a;
    --ink-soft: #4a4f55;
    --accent: #0aa3e6;
    --drop-tone: #3a4652;
    --on-dark: #ffffff;
  }
  * { box-sizing: border-box; margin: 0; padding: 0; }
  html, body {
    width: 1200px; height: 803px; overflow: hidden;
    background: var(--backdrop);
    font-family: "Arimo", Arial, sans-serif;
  }
  .stage {
    position: relative; width: 1200px; height: 803px;
    display: flex; align-items: center; justify-content: center; gap: 60px;
  }
  .card {
    position: relative; width: 525px; height: 300px;
    border-radius: 22px; overflow: hidden;
    box-shadow: 0 14px 30px rgba(0,0,0,.45);
  }
  /* Front */
  .card--front { background: var(--card-white); }
  .front-art { position: absolute; inset: 0; }
  .website {
    position: absolute; right: 14px; bottom: 24px;
    writing-mode: vertical-rl; transform: rotate(180deg);
    color: var(--on-dark); font-size: 11px; letter-spacing: .3px;
    white-space: nowrap; line-height: 1;
  }
  .identity { position: absolute; left: 36px; top: 58px; }
  .brand {
    display: flex; align-items: center; gap: 8px;
    color: var(--ink); font-size: 24px; font-weight: 400; letter-spacing: .5px;
  }
  .brand-dot { width: 11px; height: 11px; border-radius: 50%; background: var(--accent); }
  .person { margin-top: 34px; }
  .person-name { color: var(--ink); font-size: 21px; font-weight: 700; }
  .person-title { color: var(--accent); font-size: 13px; margin-top: 2px; }
  .contacts { margin-top: 20px; list-style: none; color: var(--ink-soft); font-size: 12.5px; }
  .contacts li { display: flex; align-items: center; gap: 9px; line-height: 19px; }
  .contacts svg { width: 11px; height: 11px; fill: var(--ink); }
  .abn { margin-top: 12px; color: var(--ink-soft); font-size: 12.5px; }
  /* Back */
  .card--back { background: var(--card-dark); border: 2px solid #e8e8e8; }
  .drop-field {
    position: absolute; inset: 0;
    background: linear-gradient(120deg, #12161b 0%, #1e232a 45%, var(--drop-tone) 100%);
  }
  .back-brand {
    position: absolute; left: 0; right: 0; top: 50%; transform: translateY(-50%);
    display: flex; justify-content: center; align-items: center; gap: 12px;
    color: var(--on-dark); font-size: 30px; font-weight: 400; letter-spacing: 1px;
  }
  .back-brand .brand-dot { width: 14px; height: 14px; }
</style>
</head>
<body>
<main class="stage">
  <section class="card card--front">
    <svg class="front-art" viewBox="0 0 525 300" width="525" height="300" aria-hidden="true">
      <path d="M330 0 C430 50 470 190 385 300 L525 300 L525 0 Z" fill="var(--card-dark)"/>
      <path d="M330 0 C430 50 470 190 385 300" fill="none" stroke="var(--accent)" stroke-width="5"/>
      <path d="M324 0 C422 50 462 190 378 300" fill="none" stroke="var(--card-white)" stroke-width="4"/>
    </svg>
    <p class="website">www.rvb-plumbing.com</p>
    <div class="identity">
      <div class="brand"><span class="brand-dot"></span><span>RVB Plumbing Services</span></div>
      <div class="person">
        <p class="person-name">Owen Tredgold</p>
        <p class="person-title">Director</p>
      </div>
      <ul class="contacts">
        <li><svg viewBox="0 0 24 24"><path d="M6.6 10.8a15 15 0 0 0 6.6 6.6l2.2-2.2a1 1 0 0 1 1-.25 11.4 11.4 0 0 0 3.6.57 1 1 0 0 1 1 1V20a1 1 0 0 1-1 1A17 17 0 0 1 3 4a1 1 0 0 1 1-1h3.5a1 1 0 0 1 1 1c0 1.25.2 2.45.57 3.57a1 1 0 0 1-.25 1z"/></svg>0431 862 507</li>
        <li><svg viewBox="0 0 24 24"><path d="M2 5h20v14H2z M2 5l10 8 10-8" /></svg>owen@rvb-plumbing.com.au</li>
      </ul>
      <p class="abn">ABN - 73 215 904 386</p>
    </div>
  </section>

  <section class="card card--back">
    <div class="drop-field" role="img" aria-label="Pattern of embossed water droplets on dark background"></div>
    <div class="back-brand"><span class="brand-dot"></span><span>RVB Plumbing Services</span></div>
  </section>
</main>
</body>
</html>
```